Valmuna - Plant extraction for human use

Valmuna is a plant extraction based on long pepper containing a high concentration of piperlongumine. Piperlongumine has mainly anti-cancer properties, shown in many animal studies (200). It has as well shown to inhibit dementia and bone inflammation (in animal studies). We are the first to offer this extract for the European market. Because the product will be sold under a ‘plant extraction’ legislation, we cannot make any claims about the medical properties of the extract. I need a design for the packaging (blister pack) in a category for life enhancing medicine with no connotation of cancer for the European market in a first phase. We target people from 35-75 years old. For the younger group of people, we would propose (without saying) to use our product for chemoprevention against cancer. For those patients which have been diagnosed with cancer, we would propose to use it in conjunction with chemo-radio or immunotherapy (without saying).
Target Market(s)
Europe
Look and feel

```html
<!DOCTYPE html>
<html lang="en">
<head>
<meta charset="utf-8">
<title>Valmuna – Packaging</title>
<link rel="stylesheet" href="https://fonts.googleapis.com/css2?family=Roboto+Condensed:wght@700&family=Open+Sans:wght@400;600&display=swap">
<style>
  :root {
    --green: #8cc83c;
    --green-light: #b8de62;
    --green-deep: #76b52a;
    --paper: #ffffff;
    --page: #ffffff;
    --frame: #d8d8d8;
    --ink: #333333;
  }
  * { margin: 0; padding: 0; box-sizing: border-box; }
  html, body {
    width: 1112px;
    height: 1200px;
    overflow: hidden;
    background: var(--page);
  }
  .board {
    position: relative;
    width: 1112px;
    height: 1200px;
    border: 1px solid var(--frame);
  }
  .brand-mark {
    position: absolute;
    left: 156px;
    top: 150px;
    display: flex;
    align-items: center;
    gap: 16px;
  }
  .brand-mark .dot {
    width: 34px;
    height: 34px;
    border-radius: 50%;
    background: var(--green);
  }
  .brand-name {
    font-family: "Roboto Condensed", sans-serif;
    font-weight: 700;
    color: var(--green);
    font-size: 96px;
    line-height: 1;
    letter-spacing: 1px;
  }
  .box-front {
    position: absolute;
    left: 156px;
    top: 420px;
    width: 800px;
    height: 608px;
    background: var(--paper);
    box-shadow: 0 0 0 1px #e6e6e6, 0 6px 18px rgba(0,0,0,0.12);
    overflow: hidden;
  }
  .front-logo {
    position: absolute;
    left: 40px;
    top: 56px;
    display: flex;
    align-items: center;
    gap: 14px;
  }
  .front-logo .dot {
    width: 26px;
    height: 26px;
    border-radius: 50%;
    background: var(--green);
  }
  .front-logo .brand-name { font-size: 88px; }
  .ingredient-title {
    position: absolute;
    left: 200px;
    top: 150px;
    width: 300px;
    text-align: right;
    font-family: "Open Sans", sans-serif;
    font-size: 19px;
    letter-spacing: 3px;
    color: var(--ink);
  }
  .side-panel {
    position: absolute;
    right: 0;
    top: 0;
    width: 249px;
    height: 608px;
  }
  .side-panel svg { display: block; }
  .count-badge {
    position: absolute;
    right: 79px;
    top: 38px;
    width: 92px;
    height: 92px;
    border-radius: 50%;
    background: var(--paper);
    border: 4px solid var(--green-light);
    display: flex;
    flex-direction: column;
    align-items: center;
    justify-content: center;
    gap: 4px;
  }
  .count-badge .pills { display: block; }
  .count-badge .count {
    font-family: "Roboto Condensed", sans-serif;
    font-weight: 700;
    font-size: 12px;
    color: var(--green);
    letter-spacing: 0.5px;
  }
  .divider {
    position: absolute;
    left: 0;
    top: 398px;
    width: 551px;
    height: 8px;
    background: var(--green);
  }
  .info-band {
    position: absolute;
    left: 0;
    top: 412px;
    width: 551px;
    height: 196px;
    background: linear-gradient(90deg, var(--green-deep), var(--green));
  }
  .info-card {
    position: absolute;
    left: 56px;
    top: 8px;
    right: 0;
    bottom: 14px;
    background: var(--paper);
    padding: 82px 0 0 20px;
    font-family: "Open Sans", sans-serif;
    font-size: 16px;
    line-height: 1.35;
    color: var(--ink);
  }
</style>
</head>
<body>
<main class="board">
  <div class="brand-mark">
    <span class="dot"></span>
    <span class="brand-name">VALMUNA</span>
  </div>

  <section class="box-front">
    <div class="front-logo">
      <span class="dot"></span>
      <span class="brand-name">VALMUNA</span>
    </div>
    <p class="ingredient-title">Piperlongumine</p>

    <div class="side-panel">
      <svg width="249" height="608" role="img" aria-label="Green panel with soft flowing wave lines">
        <defs>
          <linearGradient id="panelGrad" x1="0" y1="0" x2="1" y2="1">
            <stop offset="0" stop-color="#86c536"/>
            <stop offset="0.55" stop-color="#9fd247"/>
            <stop offset="1" stop-color="#bfe06a"/>
          </linearGradient>
        </defs>
        <rect width="249" height="608" fill="url(#panelGrad)"/>
      </svg>
      <div class="count-badge">
        <svg class="pills" width="34" height="20" aria-hidden="true">
          <circle cx="11" cy="10" r="9" fill="#8cc83c"/>
          <circle cx="23" cy="10" r="9" fill="#a9d857"/>
        </svg>
        <span class="count">20 CAPLETS</span>
      </div>
    </div>

    <div class="divider"></div>
    <div class="info-band">
      <div class="info-card">
        <p>Piperlongumine</p>
        <p>500mg (+) 30mg for oral use</p>
      </div>
    </div>
  </section>
</main>
</body>
</html>
```